Funhaven - launching a new children's entertainment venue

Create a flyer (to be used online and offline) to promote a new business

Business name (tbc). Current considerations are:
# "Bramblewood for KIDS"
# "BW for KIDS"
# "BW Parties"

Concept
# A creative play space for young children
# To be used for either (i) birthday parties or (ii) general play area available for Mums/parents groups to hire

Facilities:
# General play space
# Basketball, soccer
# Ball pit
# Video games
# Movies

Room designed for 2-8 year olds in mind

Catering available:
# Party pies, sausage rolls and mini franks
# Potato chips
# Cordial and water
Note - cake not included
Kitchen facility available.

Party host

Use of parents retreat room

Packages (costs):
# 2 hour party with catering pack and host $220 (up to 10 children, $17.50 per child for additional children)
# 2 hour party - BYO and host $200 (up to 10 children, $15 per child for additional children)
# Casual hire (exclusive use of room and parents retreat) - $50 per hour

Note - we also require a new logo for this new business concept

Existing business is called Bramblewood Sports, a basketball training and development facility. The new business needs to be linked to Bramblewood Sports from a banding perspective although does require its own identity

Brand essence - fun, vibrant, colourful, engaging
Updates

Project Deadline Extended Reason: Due to other projects we have been unable to review designs until tomorrow. Therefore we have opened deadline date. Added Monday, October 10, 2016

Target Market(s)

Mums of children aged 2-8 years

Industry/Entity Type

Entertainment

Logo Text

Name "Bramblewood for KIDS" (although name is not 100% confirmed)

Font styles to use
Serif
Sans Serif

Requirements
Must have
• Must be vibrant, colourful and fun
• Get across sense of energy
Nice to have
• Some sort of link to existing business "Bramblewood Sports" logos are attached
• Although we have an open mind to a totally seperate brand

```html
<!DOCTYPE html>
<html lang="en">
<head>
<meta charset="utf-8">
<title>Bramblewood for KIDS – Party Flyer</title>
<link href="https://fonts.googleapis.com/css2?family=Archivo:wght@900&family=Roboto+Condensed:wght@800&family=Cabin+Condensed:wght@600;700&family=Roboto:wght@500&display=swap" rel="stylesheet">
<style>
  :root{
    --page:#e9e9e9;
    --white:#ffffff;
    --sky:#0aa3e2;
    --sky-deep:#0580c9;
    --lime:#f2e500;
    --grass:#1e9b2e;
    --ink:#1b1b1b;
    --party-red:#d9261f;
    --warm:#f3c7a6;
  }
  *{margin:0;padding:0;box-sizing:border-box}
  html,body{width:1200px;height:1200px;overflow:hidden;background:var(--page)}
  .flyer{position:absolute;left:190px;top:20px;width:820px;height:1160px;background:var(--white);overflow:hidden;box-shadow:0 6px 24px rgba(0,0,0,.18)}
  .flyer-art{position:absolute;inset:0}
  .title{position:absolute;left:44px;top:34px;line-height:.95}
  .title-main{display:block;font-family:"Roboto Condensed",sans-serif;font-weight:800;font-size:62px;color:var(--grass);letter-spacing:.5px}
  .title-sub{display:block;font-family:"Archivo",sans-serif;font-weight:900;font-size:66px;color:var(--sky-deep)}
  .section-tab{position:absolute;left:0;height:42px;padding:0 30px 0 50px;background:var(--lime);border-radius:0 22px 22px 0;font-family:"Roboto",sans-serif;font-weight:500;font-size:20px;color:var(--ink);display:flex;align-items:center;box-shadow:0 3px 4px rgba(0,0,0,.18)}
  .tab-facilities{top:352px}
  .tab-catering{top:566px}
  .tab-packages{top:872px;padding-left:90px}
  .list{position:absolute;list-style:none;font-family:"Cabin Condensed",sans-serif;font-weight:600;color:var(--white);font-size:22px;line-height:33px}
  .list li{position:relative;padding-left:22px}
  .list li::before{content:"";position:absolute;left:2px;top:14px;width:7px;height:7px;border-radius:50%;background:var(--lime)}
  .list li.sub{padding-left:44px}
  .list li.sub::before{left:26px;border-radius:0;background:var(--white);width:6px;height:6px}
  .facilities-a{left:84px;top:410px}
  .facilities-b{left:288px;top:410px}
  .age-note{position:absolute;left:106px;top:504px;font-family:"Cabin Condensed",sans-serif;font-weight:600;font-size:22px;color:var(--white)}
  .catering{left:110px;top:628px}
  .packages{position:absolute;left:70px;top:940px;width:560px;list-style:none;font-family:"Roboto",sans-serif;font-weight:500;font-size:17px;line-height:23px;color:var(--ink)}
  .packages li{position:relative;padding-left:24px;margin-bottom:16px}
  .packages li::before{content:"";position:absolute;left:2px;top:8px;width:8px;height:8px;border-radius:50%;background:var(--sky)}
  .price{color:var(--sky)}
  .sports-mark{position:absolute;left:640px;top:1030px;display:flex;align-items:center;gap:10px;font-family:"Cabin Condensed",sans-serif;font-weight:700;font-size:20px;color:var(--ink);line-height:1.1}
  .sports-mark .square{width:44px;height:44px;background:var(--ink)}
</style>
</head>
<body>
<main class="flyer">
  <svg class="flyer-art" viewBox="0 0 820 1160" width="820" height="1160">
    <defs>
      <linearGradient id="hero-tone" x1="0" y1="0" x2="1" y2="1">
        <stop offset="0" stop-color="#f6d7c0"/>
        <stop offset=".45" stop-color="#e8a98a"/>
        <stop offset="1" stop-color="#d9261f"/>
      </linearGradient>
      <linearGradient id="mum-tone" x1="0" y1="0" x2="1" y2="1">
        <stop offset="0" stop-color="#8a5a44"/>
        <stop offset=".5" stop-color="#f3cdb6"/>
        <stop offset="1" stop-color="#e46b6b"/>
      </linearGradient>
      <linearGradient id="room-tone" x1="0" y1="0" x2="1" y2="1">
        <stop offset="0" stop-color="#d8323a"/>
        <stop offset="1" stop-color="#4b4c86"/>
      </linearGradient>
      <linearGradient id="turf-tone" x1="0" y1="0" x2="0" y2="1">
        <stop offset="0" stop-color="#c9c9c9"/>
        <stop offset="1" stop-color="#3f8a34"/>
      </linearGradient>
    </defs>

    <!-- swoosh bands -->
    <path d="M0,190 C160,200 290,230 420,290 L420,320 C290,260 160,240 0,240 Z" fill="var(--grass)"/>
    <path d="M0,222 C170,232 300,262 430,318 L430,350 C300,300 160,285 0,290 Z" fill="var(--lime)"/>

    <!-- blue body -->
    <path d="M0,290 C170,280 320,300 470,360 C620,420 720,470 820,470 L820,800 C640,860 480,820 330,800 C200,785 90,800 0,860 Z" fill="var(--sky)"/>
    <!-- lower yellow curve -->
    <path d="M0,860 C90,800 200,785 330,800 C480,820 640,860 820,800 L820,820 C640,885 470,850 330,830 C200,815 100,830 0,890 Z" fill="var(--lime)"/>

    <!-- hero party photo -->
    <circle cx="720" cy="200" r="300" fill="var(--grass)"/>
    <circle cx="728" cy="200" r="292" fill="var(--lime)"/>
    <circle cx="732" cy="196" r="284" fill="url(#hero-tone)" role="img" aria-label="Photo: excited children in party hats celebrating a birthday with a wrapped gift"/>

    <!-- small mum & child photo -->
    <circle cx="305" cy="255" r="96" fill="var(--lime)"/>
    <circle cx="305" cy="255" r="88" fill="url(#mum-tone)" role="img" aria-label="Photo: mother and young daughter playing with stacking cups"/>

    <!-- room photos -->
    <circle cx="700" cy="610" r="98" fill="var(--lime)"/>
    <circle cx="700" cy="610" r="90" fill="url(#room-tone)" role="img" aria-label="Photo: play room with red and purple walls, armchairs and an arcade game table"/>
    <circle cx="585" cy="790" r="74" fill="var(--lime)"/>
    <circle cx="585" cy="790" r="67" fill="url(#turf-tone)" role="img" aria-label="Photo: play area with artificial turf, blue benches and coloured cubbies"/>
    <circle cx="745" cy="782" r="70" fill="var(--lime)"/>
    <circle cx="745" cy="782" r="63" fill="url(#turf-tone)" role="img" aria-label="Photo: child sitting on blue benches in the turf play area"/>
  </svg>

  <h1 class="title">
    <span class="title-main">BRAMBLEWOOD</span>
    <span class="title-sub">FOR KIDS</span>
  </h1>

  <div class="section-tab tab-facilities">FACILITIES:</div>
  <ul class="list facilities-a">
    <li>General play space</li>
    <li>Basketball, soccer</li>
    <li>Ball pit</li>
  </ul>
  <ul class="list facilities-b">
    <li>Video games</li>
    <li>Movies</li>
  </ul>
  <p class="age-note">Room designed for 2-8 year olds in mind</p>

  <div class="section-tab tab-catering">CATERING AVAILABLE:</div>
  <ul class="list catering">
    <li>Party pies, sausage rolls and mini franks</li>
    <li class="sub">Potato chips</li>
    <li class="sub">Cordial and water</li>
    <li>Note - cake not included</li>
    <li>Kitchen facility available.</li>
  </ul>

  <div class="section-tab tab-packages">PACKAGES (COSTS):</div>
  <ul class="packages">
    <li>2 hour party with catering pack and host <span class="price">$220</span><br>(up to 10 children, <span class="price">$17.50</span> per child for additional children)</li>
    <li>2 hour party - BYO and host <span class="price">$200</span> (up to 10 children,<br><span class="price">$15</span> per child for additional children)</li>
    <li>Casual hire<br>(exclusive use of room and parents retreat)<br><span class="price">$50</span> per hour</li>
  </ul>

  <div class="sports-mark"><span class="square"></span><span>Bramblewood<br>Sports</span></div>
</main>
</body>
</html>
```